Brisco Energy PowerPoint Design

Looking for a sleek PowerPoint design for our energy services company. We supply EV charging, Solar, Battery Storage and more.

Please make the background white with hints of gray and utilize the exact dark blue and light blue colors in the logo.

This design should be sharp with minimal round edges.

Colors

Designer to choose colors to be used in the design.

```html
<!DOCTYPE html>
<html lang="en">
<head>
<meta charset="utf-8">
<title>Brisco Energy – Presentation Slides</title>
<link href="https://fonts.googleapis.com/css2?family=Roboto:ital,wght@0,300;0,400;0,500;0,700;1,300;1,400&display=swap" rel="stylesheet">
<style>
:root{
  --navy:#15105f;
  --sky:#3db4ea;
  --blue:#1f8bf2;
  --gray:#dcdcdc;
  --line:#c9c9c9;
  --text:#555;
  --mute:#9a9a9a;
  --page:#ffffff;
}
*{box-sizing:border-box}
html,body{margin:0;width:1200px;height:1200px;overflow:hidden;background:var(--page)}
body{position:relative;font-family:Roboto,sans-serif;color:var(--text)}
.slide{position:absolute;width:261px;height:146px;background:#fff;box-shadow:6px 8px 14px rgba(0,0,0,.26);overflow:hidden}
.c1{left:108px}.c2{left:473px}.c3{left:838px}
.r1{top:47px}.r2{top:209px}.r3{top:369px}.r4{top:531px}.r5{top:691px}.r6{top:852px}.r7{top:1013px}
.a{position:absolute}
.photo{position:absolute}
.brand{position:absolute;display:flex;align-items:center;gap:2px;color:var(--navy);font-weight:700;font-size:5px;white-space:nowrap;letter-spacing:.1px}
.brand i{display:block;width:6px;height:6px;background:var(--navy)}
.brand.lg{font-size:7px;gap:3px}.brand.lg i{width:9px;height:9px}
.brand.sm{font-size:3.4px}.brand.sm i{width:4px;height:4px}
.brand.white{color:#fff}.brand.white i{background:#fff}
.foot{position:absolute;left:15px;bottom:4px;font-size:5px;color:var(--navy);white-space:nowrap}
.foot small{font-size:2px;margin-left:1px}
.pg{position:absolute;right:15px;bottom:5.5px;font-size:2px;color:var(--mute);white-space:nowrap}
.p{font-size:2.6px;line-height:1.6;color:#777}
.pl{font-size:4.2px;line-height:1.25;color:#555}
.it{font-style:italic;font-size:3.6px;line-height:1.55;color:#666}
.h{font-weight:500;color:var(--navy)}
.ttl{font-size:7.5px;font-weight:500;color:var(--navy)}
.blk{font-size:3.4px;line-height:1.25;color:#333}
.blk b{display:block;font-weight:400;font-size:4px;color:#222}
.rule{position:absolute;height:.5px;background:var(--line)}
.dot{position:absolute;width:10px;height:10px;border-radius:50%;background:var(--navy);display:flex;align-items:center;justify-content:center}
.dot.sky{background:var(--sky)}
.dot svg{width:5px;height:5px}
.item{position:absolute;font-size:2.6px;line-height:1.5;color:#888}
.item b{display:block;font-size:3px;color:#222;font-weight:500}
.sub{font-size:2px;color:var(--mute)}
.bars{position:absolute;display:flex;align-items:flex-end;justify-content:space-between}
.bar{display:flex;flex-direction:column;width:6px}
.bar .t{background:var(--sky)}.bar .b{background:var(--navy)}
.months{position:absolute;display:flex;justify-content:space-between;font-size:1.8px;color:var(--mute)}
.legend{position:absolute;font-size:2px;color:var(--mute);line-height:3.4}
.legend span{display:inline-block;width:2px;height:2px;margin-right:2px;vertical-align:middle}
table{border-collapse:collapse}
.grid td,.grid th{border:.5px solid #333;font-size:2px;font-weight:400;padding:0}
.grid th{background:var(--blue);color:#fff;height:11px}
.grid td{height:12.9px;color:#333;text-align:center}
.cal td,.cal th{border:.4px solid #bbb;font-size:1.8px;font-weight:400;text-align:left;vertical-align:top;padding:1px}
.cal th{background:var(--blue);color:#fff;height:5px;border-color:var(--blue)}
.cal td{height:15.5px;color:#444;position:relative}
.ev{position:absolute;left:1px;top:5px;height:2.6px;background:var(--blue);color:#fff;font-size:1.6px;padding-left:1px}
.pct{position:absolute;font-size:19px;font-weight:300;color:var(--navy);left:130px}
.pct.sky{color:var(--sky)}
.ring{position:absolute;width:45px;height:45px;border-radius:50%;display:flex;align-items:center;justify-content:center;font-size:9px;font-weight:500;color:#333}
</style>
</head>
<body>

<!-- Row 1 -->
<section class="slide c1 r1">
  <div class="a" style="left:152px;top:0;width:109px;height:146px;background:var(--gray)"></div>
  <div class="a" style="left:28px;top:11px;font-size:3.4px;letter-spacing:.7px;color:#333">www.brisco-energy.xyz</div>
  <svg class="a" style="left:235px;top:9px" width="7" height="5" viewBox="0 0 7 5"><path d="M0 .5h7M0 2.5h7M0 4.5h7" stroke="var(--blue)" stroke-width=".7"/></svg>
  <div class="photo" role="img" aria-label="Hand plugging a charging cable into an electric car" style="left:2px;top:24px;width:181px;height:90px;background:linear-gradient(115deg,#5f8a57 0%,#a7b9a3 30%,#e9edf0 50%,#8fa4bf 72%,#2f4f8a 100%);box-shadow:2px 3px 6px rgba(0,0,0,.25)"></div>
  <div class="brand lg" style="left:189px;top:44px">Brisco Energy</div>
  <div class="a" style="left:189px;top:78px;font-size:9px;line-height:1.1;color:var(--navy)">Empowering<br>Renewable<br>Solutions</div>
  <div class="a" style="left:28px;top:123px;font-size:3.4px;line-height:1.8;color:#222"><b style="font-weight:500">Presented by: Dana Mercer</b><br>November 2024</div>
  <div class="rule" style="left:66px;top:132px;width:11px;background:var(--blue)"></div>
  <div class="pg" style="right:115px">www.brisco-energy.xyz</div>
</section>

<section class="slide c2 r1">
  <div class="brand" style="left:17px;top:38px">Brisco Energy</div>
  <div class="a ttl" style="left:54px;top:39px">Welcome</div>
  <div class="rule" style="left:17px;top:61px;width:10px"></div>
  <div class="a p" style="left:17px;top:69px;width:90px">Lorem ipsum is simply dummy text of the printing and typesetting industry. Lorem ipsum has been the standard dummy text ever since the 1500s, when an unknown printer took a galley of type and scrambled it.</div>
  <div class="a" style="left:70px;top:107px;font-size:4px;color:#222;font-weight:500">Dana Mercer</div>
  <div class="photo" role="img" aria-label="Charging plug connected to a silver electric car" style="left:131px;top:21px;width:115px;height:104px;background:linear-gradient(150deg,#5f6c62 0%,#c9ced3 40%,#9aa3ad 65%,#3f4650 100%)"></div>
  <div class="foot">Brisco Energy <small>a renewable energy services company</small></div>
  <div class="pg">www.brisco-energy.xyz &nbsp;|&nbsp; 2</div>
</section>

<section class="slide c3 r1">
  <div class="photo" role="img" aria-label="Solar farm and wind turbine at sunset" style="left:0;top:21px;width:147px;height:104px;background:linear-gradient(180deg,#3c5aa0 0%,#a98aa8 35%,#eaa878 50%,#5d6a8a 60%,#2c3966 100%)"></div>
  <div class="brand white" style="left:50px;top:68px">Brisco Energy</div>
  <div class="a" style="left:162px;top:24px;font-size:7.5px;font-weight:700;color:var(--navy)">Who We Are</div>
  <div class="a" style="left:162px;top:35px;font-size:4px;color:#666">Empowering Renewable Solutions</div>
  <div class="a it" style="left:162px;top:50px;width:85px;font-size:2.9px">Brisco Energy is a renewable energy services company that offers complete solutions to meet our customers' renewable energy needs. We handle everything from design and engineering to the supply of software, hardware, and installation.</div>
  <div class="a p" style="left:162px;top:98px;width:85px">Lorem ipsum is simply dummy text of the printing and typesetting industry. Lorem ipsum has been the standard dummy text ever since the 1500s.</div>
  <div class="foot">Brisco Energy <small>a renewable energy services company</small></div>
  <div class="pg">www.brisco-energy.xyz &nbsp;|&nbsp; 3</div>
</section>

<!-- Row 2 -->
<section class="slide c1 r2">
  <div class="photo" role="img" aria-label="Wall-mounted chargers beside a parked car" style="left:0;top:21px;width:147px;height:104px;background:linear-gradient(90deg,#8b9096 0%,#4b4f55 35%,#2a2d31 65%,#4a4f56 100%)"></div>
  <div class="brand" style="left:154px;top:30px">Brisco Energy</div>
  <div class="a it" style="left:188px;top:29px;width:60px">Lorem ipsum is simply dummy text of the printing</div>
  <div class="rule" style="left:154px;top:55px;width:10px"></div>
  <div class="a p" style="left:154px;top:62px;width:92px">Lorem ipsum is simply dummy text of the printing and typesetting industry. Lorem ipsum has been the standard dummy text ever since the 1500s, when an unknown printer took a galley of type.</div>
  <div class="a pl" style="left:154px;top:100px;width:92px">Lorem ipsum is simply dummy text of the printing and typesetting industry.</div>
  <div class="foot">Brisco Energy <small>a renewable energy services company</small></div>
  <div class="pg">www.brisco-energy.xyz &nbsp;|&nbsp; 4</div>
</section>

<section class="slide c2 r2">
  <div class="brand" style="left:13px;top:29px">Brisco Energy</div>
  <div class="a it" style="left:48px;top:28px;width:60px">Lorem ipsum is simply dummy text of the printing</div>
  <div class="rule" style="left:13px;top:54px;width:10px"></div>
  <div class="a p" style="left:13px;top:61px;width:92px">Lorem ipsum is simply dummy text of the printing and typesetting industry. Lorem ipsum has been the standard dummy text ever since the 1500s, when an unknown printer took a galley.</div>
  <div class="a pl" style="left:13px;top:100px;width:92px">Lorem ipsum is simply dummy text of the printing and typesetting industry.</div>
  <div class="photo" role="img" aria-label="Row of fast charging stations in a car park" style="left:115px;top:0;width:73px;height:146px;background:linear-gradient(180deg,#c8d3de 0%,#e4e7ea 40%,#9aa89a 75%,#6fb55e 100%)"></div>
  <div class="photo" role="img" aria-label="Wall charger next to a dark car outside a house" style="left:188px;top:0;width:73px;height:146px;background:linear-gradient(160deg,#6f8f4a 0%,#c9c4b5 45%,#e8e6e2 60%,#3b3f44 100%)"></div>
  <div class="foot">Brisco Energy <small>a renewable energy services company</small></div>
</section>

<section class="slide c3 r2">
  <div class="brand sm" style="left:232px;top:7px">Brisco</div>
  <div class="photo" role="img" aria-label="Solar panels on green grass" style="left:0;top:21px;width:131px;height:52px;background:linear-gradient(135deg,#3c4a63 0%,#6d8f4d 45%,#45516a 70%,#7ea256 100%)"></div>
  <div class="a blk" style="left:141px;top:27px;width:105px"><b>Site Assessment</b>At Brisco Energy, we ensure your project's success by conducting detailed site surveys. Our team evaluates the unique features of your property to determine the best placement and integration for EV chargers, solar systems, and battery storage.</div>
  <div class="a blk" style="left:19px;top:84px;width:104px"><b>EV Charging</b>We know that expert installation is crucial for your energy solutions. That's why we collaborate with skilled installation partners who specialize in EV chargers, solar panels, and energy storage systems, making the process smooth.</div>
  <div class="photo" role="img" aria-label="Charging cable plugged into an electric car" style="left:131px;top:73px;width:130px;height:52px;background:linear-gradient(120deg,#e6eaee 0%,#aab5c2 50%,#5a6a80 100%)"></div>
  <div class="foot">Brisco Energy <small>a renewable energy services company</small></div>
  <div class="pg">www.brisco-energy.xyz &nbsp;|&nbsp; 6</div>
</section>

<!-- Row 3 -->
<section class="slide c1 r3">
  <div class="brand sm" style="left:232px;top:7px">Brisco</div>
  <div class="photo" role="img" aria-label="Battery storage cabinets in a field" style="left:0;top:21px;width:131px;height:52px;background:linear-gradient(180deg,#cfd3d6 0%,#dcdedf 40%,#9a9e9f 65%,#6e7e55 100%)"></div>
  <div class="a blk" style="left:141px;top:27px;width:110px"><b>Engineering</b>Our commitment to excellence includes having experienced engineers plan every aspect of your site. They work closely with our installation partners to create precise designs for your EV charging stations, solar installations, and battery storage.</div>
  <div class="a blk" style="left:19px;top:84px;width:104px"><b>Financing</b>We understand that investing in sustainable energy should be accessible. That's why we provide a range of financing options to help you manage the costs of your EV charging stations, solar installations, and battery storage.</div>
  <div class="photo" role="img" aria-label="Calculator, pen and printed bar chart" style="left:131px;top:73px;width:130px;height:52px;background:linear-gradient(120deg,#3a3a3c 0%,#8c8c8e 35%,#e4e4e4 60%,#bdbdbd 100%)"></div>
  <div class="foot">Brisco Energy <small>a renewable energy services company</small></div>
  <div class="pg">www.brisco-energy.xyz &nbsp;|&nbsp; 7</div>
</section>

<section class="slide c2 r3">
  <div class="photo" role="img" aria-label="Wall chargers with orange bollards beside a car" style="left:0;top:0;width:261px;height:73px;background:linear-gradient(90deg,#6c7178 0%,#3c4046 35%,#2a2d31 60%,#1f3350 100%)"></div>
  <div class="brand lg" style="left:17px;top:100px">Brisco Energy</div>
  <div class="a" style="left:61px;top:98px;font-size:7.5px;color:var(--navy);display:none"></div>
  <div class="a" style="left:17px;top:90px;font-size:7px;color:var(--navy);display:none"></div>
  <div class="a" style="left:72px;top:99px;font-size:7.2px;color:var(--navy)">DC Fast Charging</div>
  <div class="a p" style="left:134px;top:89px;width:115px">For rapid charging needs, we provide access to DC Fast Charging stations that dramatically reduce charging times. Perfect for businesses and public spaces, these systems deliver high power output.</div>
  <div class="a" style="left:134px;top:111px;font-size:2.4px;color:var(--sky)">See our DC Fast Charging page for more information</div>
  <div class="foot">Brisco Energy <small>a renewable energy services company</small></div>
  <div class="pg">www.brisco-energy.xyz &nbsp;|&nbsp; 8</div>
</section>

<section class="slide c3 r3">
  <div class="brand lg" style="left:17px;top:34px">Brisco Energy</div>
  <div class="a" style="left:72px;top:33px;font-size:7.2px;color:var(--navy)">Level 2 Charging</div>
  <div class="a p" style="left:134px;top:22px;width:115px">We offer Level 2 charging solutions that provide reliable and efficient power for electric vehicles in commercial environments. These systems are designed for optimal charging speeds.</div>
  <div class="a" style="left:134px;top:48px;font-size:2.4px;color:var(--sky)">See our Level 2 Charging page for more information</div>
  <div class="photo" role="img" aria-label="Hand plugging a charging cable into an electric car" style="left:0;top:63px;width:261px;height:83px;background:linear-gradient(115deg,#e7ebef 0%,#b8c6d6 35%,#2f4f8a 55%,#6b8f5c 80%,#9bb48a 100%)"></div>
</section>

<!-- Row 4 -->
<section class="slide c1 r4">
  <div class="photo" role="img" aria-label="Charging post on a park lawn under a tree" style="left:0;top:0;width:131px;height:146px;background:linear-gradient(180deg,#476b32 0%,#6f9648 40%,#8fb15c 70%,#a9c57a 100%)"></div>
  <div class="brand" style="left:155px;top:23px">Brisco Energy</div>
  <div class="a it" style="left:189px;top:21px;width:60px">Lorem ipsum is simply dummy text of the printing</div>
  <div class="dot" style="left:155px;top:47px"><svg viewBox="0 0 10 10"><path d="M2 8L8 2M4 2h4v4" stroke="#fff" fill="none"/></svg></div>
  <div class="item" style="left:171px;top:48px;width:62px"><b>CONSULTING PLAN</b>Quickly repurpose top-line innovation before global communities</div>
  <div class="dot sky" style="left:155px;top:67px"><svg viewBox="0 0 10 10"><rect x="2" y="2" width="6" height="6" fill="none" stroke="#fff"/></svg></div>
  <div class="item" style="left:171px;top:68px;width:62px"><b>CONSULTING PLAN</b>Quickly repurpose top-line innovation before global communities</div>
  <div class="dot" style="left:155px;top:87px"><svg viewBox="0 0 10 10"><path d="M2 8L8 2M4 2h4v4" stroke="#fff" fill="none"/></svg></div>
  <div class="item" style="left:171px;top:88px;width:62px"><b>CONSULTING PLAN</b>Quickly repurpose top-line innovation before global communities</div>
  <div class="dot sky" style="left:155px;top:107px"><svg viewBox="0 0 10 10"><rect x="2" y="2" width="6" height="6" fill="none" stroke="#fff"/></svg></div>
  <div class="item" style="left:171px;top:108px;width:62px"><b>CONSULTING PLAN</b>Quickly repurpose top-line innovation before global communities</div>
  <div class="pg">www.brisco-energy.xyz &nbsp;|&nbsp; 10</div>
</section>

<section class="slide c2 r4">
  <div class="photo" role="img" aria-label="Electrical substation under a pink evening sky" style="left:0;top:0;width:131px;height:146px;background:linear-gradient(180deg,#5c7fb5 0%,#c9a2bb 30%,#8a97b0 50%,#4a5e78 75%,#3f6b3a 100%)"></div>
  <div class="brand" style="left:152px;top:30px">Brisco Energy</div>
  <div class="a it" style="left:186px;top:27px;width:60px">Lorem ipsum is simply dummy text of the printing</div>
  <div class="a p" style="left:152px;top:52px;width:95px">Lorem ipsum is simply dummy text of the printing and typesetting industry. Lorem ipsum has been the standard dummy text ever since the 1500s, when an unknown printer took a galley of type.</div>
  <div class="dot sky" style="left:152px;top:86px"><svg viewBox="0 0 10 10"><rect x="2" y="2" width="6" height="6" fill="none" stroke="#fff"/></svg></div>
  <div class="item" style="left:168px;top:87px;width:62px"><b>CONSULTING PLAN</b>Quickly repurpose top-line innovation before global communities</div>
  <div class="dot" style="left:152px;top:106px"><svg viewBox="0 0 10 10"><path d="M2 8L8 2M4 2h4v4" stroke="#fff" fill="none"/></svg></div>
  <div class="item" style="left:168px;top:107px;width:62px"><b>CONSULTING PLAN</b>Quickly repurpose top-line innovation before global communities</div>
  <div class="pg">www.brisco-energy.xyz &nbsp;|&nbsp; 11</div>
</section>

<section class="slide c3 r4">
  <div class="a" style="left:0;top:20px;width:111px;height:53px;background:var(--navy)"></div>
  <div class="brand white" style="left:15px;top:42px">Brisco Energy</div>
  <div class="a" style="left:66px;top:38px;font-size:4.5px;font-weight:500;color:#fff;line-height:1.9">Features<br>Service</div>
  <div class="photo" role="img" aria-label="Row of charging stations in an open car park" style="left:0;top:73px;width:111px;height:52px;background:linear-gradient(180deg,#c8d3dd 0%,#d9dde0 45%,#9fa6aa 75%,#8aae7e 100%)"></div>
  <div class="pct" style="top:27px">15%</div>
  <div class="pct sky" style="top:63px">05%</div>
  <div class="pct" style="top:99px">80%</div>
  <div class="item" style="left:183px;top:32px;width:62px"><b>01. Services <span class="sub">Name</span></b>Quickly repurpose top-line innovation before global communities.</div>
  <div class="item" style="left:183px;top:68px;width:62px"><b>02. Services <span class="sub">Name</span></b>Quickly repurpose top-line innovation before global communities.</div>
  <div class="item" style="left:183px;top:104px;width:62px"><b>01. Services <span class="sub">Name</span></b>Quickly repurpose top-line innovation before global communities.</div>
  <div class="foot">Brisco Energy <small>a renewable energy services company</small></div>
  <div class="pg">www.brisco-energy.xyz &nbsp;|&nbsp; 12</div>
</section>

<!-- Row 5 -->
<section class="slide c1 r5">
  <div class="brand" style="left:17px;top:35px">Brisco Energy</div>
  <div class="a it" style="left:51px;top:33px;width:60px">Lorem ipsum is simply dummy text of the printing</div>
  <div class="a it" style="left:17px;top:60px;width:90px;font-size:2.8px">"Neque porro quisquam est qui dolorem ipsum quia dolor sit amet, consectetur, adipisci velit..."</div>
  <div class="dot" style="left:131px;top:33px;width:13px;height:13px"><svg viewBox="0 0 10 10"><rect x="2" y="3" width="6" height="4" fill="none" stroke="#fff"/></svg></div>
  <div class="item" style="left:162px;top:34px;width:75px"><b style="font-size:4px">Services <span class="sub">Name</span></b>Quickly repurpose top-line innovation before global communities.</div>
  <div class="dot sky" style="left:131px;top:68px;width:13px;height:13px"><svg viewBox="0 0 10 10"><path d="M2 5l6-3-3 6-1-2z" fill="#fff"/></svg></div>
  <div class="item" style="left:162px;top:69px;width:75px"><b style="font-size:4px">Services <span class="sub">Name</span></b>Quickly repurpose top-line innovation before global communities.</div>
  <div class="dot" style="left:131px;top:101px;width:13px;height:13px"><svg viewBox="0 0 10 10"><path d="M2 8h6M3 4v4M5 4v4M7 4v4M2 4l3-2 3 2z" stroke="#fff" fill="none" stroke-width=".8"/></svg></div>
  <div class="item" style="left:162px;top:102px;width:75px"><b style="font-size:4px">Services <span class="sub">Name</span></b>Quickly repurpose top-line innovation before global communities.</div>
  <div class="foot">Brisco Energy <small>a renewable energy services company</small></div>
  <div class="pg">www.brisco-energy.xyz &nbsp;|&nbsp; 13</div>
</section>

<section class="slide c2 r5">
  <div class="a" style="left:0;top:0;width:181px;height:133px;background:var(--navy)"></div>
  <div class="brand white sm" style="left:17px;top:11px">Brisco</div>
  <div class="a" style="left:44px;top:8px;font-size:5.2px;font-weight:500;color:#fff">Our Core Services</div>
  <div class="a" style="left:44px;top:16px;font-size:2px;color:#c8c8e0">Quickly repurpose top-line innovation before global communities</div>
  <div class="a" style="left:16px;top:32px;width:64px;font-size:2px;line-height:1.6;color:#d9d9ee"><b style="display:block;font-size:2.6px;color:#fff;font-weight:500;margin-bottom:2px">Your description text</b>Make a positive impression with this clean and strong presentation template. Everything you need for a powerful and convincing talk.</div>
  <div class="a" style="left:99px;top:32px;width:64px;font-size:2px;line-height:1.6;color:#d9d9ee"><b style="display:block;font-size:2.6px;color:#fff;font-weight:500;margin-bottom:2px">Your description text</b>Make a positive impression with this clean and strong presentation template. Everything you need for a powerful and convincing talk.</div>
  <div class="a" style="left:16px;top:89px;width:64px;font-size:2px;line-height:1.6;color:#d9d9ee"><b style="display:block;font-size:2.6px;color:#fff;font-weight:500;margin-bottom:2px">Your description text</b>Make a positive impression with this clean and strong presentation template. Everything you need for a powerful and convincing talk.</div>
  <div class="a" style="left:99px;top:89px;width:64px;font-size:2px;line-height:1.6;color:#d9d9ee"><b style="display:block;font-size:2.6px;color:#fff;font-weight:500;margin-bottom:2px">Your description text</b>Make a positive impression with this clean and strong presentation template. Everything you need for a powerful and convincing talk.</div>
  <div class="photo" role="img" aria-label="Charging post on a park lawn" style="left:181px;top:0;width:80px;height:133px;background:linear-gradient(180deg,#4a6e34 0%,#7a9f52 50%,#a8c079 100%)"></div>
  <div class="foot">Brisco Energy <small>a renewable energy services company</small></div>
  <div class="pg">www.brisco-energy.xyz &nbsp;|&nbsp; 14</div>
</section>

<section class="slide c3 r5">
  <div class="brand sm" style="left:232px;top:7px">Brisco</div>
  <div class="a" style="left:0;top:7px;width:261px;text-align:center;font-size:5.5px;font-weight:500;color:#222">Our Core Services</div>
  <div class="a sub" style="left:0;top:16px;width:261px;text-align:center">Quickly repurpose top-line innovation before global communities</div>
  <div class="dot sky" style="left:16px;top:34px;width:13px;height:13px"><svg viewBox="0 0 10 10"><rect x="2" y="2" width="6" height="6" fill="none" stroke="#fff"/></svg></div>
  <div class="item" style="left:47px;top:35px;width:65px"><b>Your description text</b>Quickly repurpose top-line innovation before global communities. Efficiently benchmark.</div>
  <div class="dot" style="left:16px;top:68px;width:13px;height:13px"><svg viewBox="0 0 10 10"><path d="M2 8L8 2M4 2h4v4" stroke="#fff" fill="none"/></svg></div>
  <div class="item" style="left:47px;top:69px;width:65px"><b>Your description text</b>Quickly repurpose top-line innovation before global communities. Efficiently benchmark.</div>
  <div class="dot sky" style="left:16px;top:102px;width:13px;height:13px"><svg viewBox="0 0 10 10"><rect x="2" y="2" width="6" height="6" fill="none" stroke="#fff"/></svg></div>
  <div class="item" style="left:47px;top:103px;width:65px"><b>Your description text</b>Quickly repurpose top-line innovation before global communities. Efficiently benchmark.</div>
  <div class="dot" style="left:152px;top:34px;width:13px;height:13px"><svg viewBox="0 0 10 10"><rect x="2" y="3" width="6" height="4" fill="none" stroke="#fff"/></svg></div>
  <div class="item" style="left:183px;top:35px;width:65px"><b>Your description text</b>Quickly repurpose top-line innovation before global communities. Efficiently benchmark.</div>
  <div class="dot sky" style="left:152px;top:68px;width:13px;height:13px"><svg viewBox="0 0 10 10"><path d="M2 5l6-3-3 6-1-2z" fill="#fff"/></svg></div>
  <div class="item" style="left:183px;top:69px;width:65px"><b>Your description text</b>Quickly repurpose top-line innovation before global communities. Efficiently benchmark.</div>
  <div class="dot" style="left:152px;top:102px;width:13px;height:13px"><svg viewBox="0 0 10 10"><path d="M2 8h6M3 4v4M5 4v4M7 4v4M2 4l3-2 3 2z" stroke="#fff" fill="none" stroke-width=".8"/></svg></div>
  <div class="item" style="left:183px;top:103px;width:65px"><b>Your description text</b>Quickly repurpose top-line innovation before global communities. Efficiently benchmark.</div>
  <div class="foot">Brisco Energy <small>a renewable energy services company</small></div>
  <div class="pg">www.brisco-energy.xyz &nbsp;|&nbsp; 15</div>
</section>

<!-- Row 6 -->
<section class="slide c1 r6">
  <div class="brand sm" style="left:232px;top:7px">Brisco</div>
  <div class="a" style="left:17px;top:12px;font-size:7px;font-weight:700;color:#111">Real Statistic</div>
  <div class="a sub" style="left:17px;top:22px">Quickly repurpose top-line innovation before global communities</div>
  <div class="a pl" style="left:17px;top:42px;width:70px;font-size:4.4px">Make a Positive Impression with this Clean and Strong Presentation Template</div>
  <div class="legend" style="left:16px;top:72px"><span style="background:var(--blue)"></span>The Chart Name<br><span style="background:var(--navy)"></span>The Chart Name</div>
  <div class="bars" style="left:24px;top:35px;width:212px;height:84px">
    <div class="bar"><div class="t" style="height:2px"></div><div class="b" style="height:4px"></div></div>
    <div class="bar"><div class="t" style="height:3px"></div><div class="b" style="height:7px"></div></div>
    <div class="bar"><div class="t" style="height:2px"></div><div class="b" style="height:5px"></div></div>
    <div class="bar"><div class="t" style="height:1px"></div><div class="b" style="height:6px"></div></div>
    <div class="bar"><div class="t" style="height:4px"></div><div class="b" style="height:16px"></div></div>
    <div class="bar"><div class="t" style="height:8px"></div><div class="b" style="height:13px"></div></div>
    <div class="bar"><div class="t" style="height:3px"></div><div class="b" style="height:12px"></div></div>
    <div class="bar"><div class="t" style="height:5px"></div><div class="b" style="height:15px"></div></div>
    <div class="bar"><div class="t" style="height:8px"></div><div class="b" style="height:15px"></div></div>
    <div class="bar"><div class="t" style="height:8px"></div><div class="b" style="height:28px"></div></div>
    <div class="bar"><div class="t" style="height:17px"></div><div class="b" style="height:38px"></div></div>
    <div class="bar"><div class="t" style="height:3px"></div><div class="b" style="height:50px"></div></div>
  </div>
  <div class="months" style="left:24px;top:121px;width:212px"><span>Jan</span><span>Feb</span><span>Mar</span><span>Apr</span><span>May</span><span>Jun</span><span>Jul</span><span>Aug</span><span>Sep</span><span>Oct</span><span>Nov</span><span>Dec</span></div>
  <div class="foot">Brisco Energy <small>a renewable energy services company</small></div>
  <div class="pg">www.brisco-energy.xyz &nbsp;|&nbsp; 16</div>
</section>

<section class="slide c2 r6">
  <div class="brand sm" style="left:232px;top:7px">Brisco</div>
  <div class="a" style="left:17px;top:13px;font-size:7px;font-weight:700;color:#111">Real Statistic</div>
  <div class="a sub" style="left:17px;top:24px">Quickly repurpose top-line innovation before global communities</div>
  <div class="a pl" style="left:17px;top:42px;width:70px">Lorem Ipsum is simply dummy text of the printing</div>
  <div class="a" style="left:16px;top:74px;width:68px;height:20px;background:var(--navy);color:#fff;font-size:7.5px;font-weight:700;padding:5px 0 0 11px">50% <span style="font-size:4px;font-weight:400">Chart Name</span></div>
  <div class="a" style="left:16px;top:97px;width:68px;height:20px;background:var(--sky);color:#fff;font-size:7.5px;font-weight:700;padding:5px 0 0 11px">10% <span style="font-size:4px;font-weight:400">Chart Name</span></div>
  <div class="legend" style="left:123px;top:56px"><span style="background:var(--sky)"></span>The Chart Name<br><span style="background:var(--navy)"></span>The Chart Name</div>
  <div class="bars" style="left:122px;top:35px;width:125px;height:84px">
    <div class="bar" style="width:1.5px"><div class="t" style="height:2px"></div><div class="b" style="height:4px"></div></div>
    <div class="bar" style="width:1.5px"><div class="t" style="height:3px"></div><div class="b" style="height:7px"></div></div>
    <div class="bar" style="width:1.5px"><div class="t" style="height:2px"></div><div class="b" style="height:5px"></div></div>
    <div class="bar" style="width:1.5px"><div class="t" style="height:1px"></div><div class="b" style="height:6px"></div></div>
    <div class="bar" style="width:1.5px"><div class="t" style="height:4px"></div><div class="b" style="height:16px"></div></div>
    <div class="bar" style="width:1.5px"><div class="t" style="height:8px"></div><div class="b" style="height:13px"></div></div>
    <div class="bar" style="width:1.5px"><div class="t" style="height:3px"></div><div class="b" style="height:12px"></div></div>
    <div class="bar" style="width:1.5px"><div class="t" style="height:5px"></div><div class="b" style="height:15px"></div></div>
    <div class="bar" style="width:1.5px"><div class="t" style="height:8px"></div><div class="b" style="height:15px"></div></div>
    <div class="bar" style="width:1.5px"><div class="t" style="height:8px"></div><div class="b" style="height:28px"></div></div>
    <div class="bar" style="width:1.5px"><div class="t" style="height:17px"></div><div class="b" style="height:38px"></div></div>
    <div class="bar" style="width:1.5px"><div class="t" style="height:3px"></div><div class="b" style="height:50px"></div></div>
  </div>
  <div class="months" style="left:120px;top:121px;width:130px"><span>Jan</span><span>Feb</span><span>Mar</span><span>Apr</span><span>May</span><span>Jun</span><span>Jul</span><span>Aug</span><span>Sep</span><span>Oct</span><span>Nov</span><span>Dec</span></div>
  <div class="foot">Brisco Energy <small>a renewable energy services company</small></div>
  <div class="pg">www.brisco-energy.xyz &nbsp;|&nbsp; 17</div>
</section>

<section class="slide c3 r6">
  <div class="brand sm" style="left:232px;top:7px">Brisco</div>
  <div class="a" style="left:17px;top:12px;font-size:5.5px;font-weight:700;color:#111">Real <span style="color:var(--blue)">Statistic</span></div>
  <div class="a sub" style="left:17px;top:21px">Quickly repurpose top-line innovation before global communities</div>
  <div class="a pl" style="left:17px;top:32px;width:105px;font-size:4px">Lorem Ipsum is simply dummy text of the printing Lorem Ipsum is simply dummy text</div>
  <div class="ring" style="left:17px;top:55px;border:2px solid var(--blue);border-left-color:#d9e6f5">60<small style="font-size:3px">%</small></div>
  <div class="ring" style="left:78px;top:55px;border:2px solid var(--blue);border-bottom-color:#d9e6f5">80<small style="font-size:3px">%</small></div>
  <div class="item" style="left:17px;top:108px;width:45px;text-align:center"><b>SERVICES NAME</b>Quickly repurpose top-line innovation before communities</div>
  <div class="item" style="left:78px;top:108px;width:45px;text-align:center"><b>SERVICES NAME</b>Quickly repurpose top-line innovation before communities</div>
  <div class="dot" style="left:152px;top:33px;width:13px;height:13px"><svg viewBox="0 0 10 10"><rect x="2" y="3" width="6" height="4" fill="none" stroke="#fff"/></svg></div>
  <div class="item" style="left:183px;top:34px;width:65px"><b>Your description text</b>Quickly repurpose top-line innovation before global communities.</div>
  <div class="dot sky" style="left:152px;top:67px;width:13px;height:13px"><svg viewBox="0 0 10 10"><path d="M2 5l6-3-3 6-1-2z" fill="#fff"/></svg></div>
  <div class="item" style="left:183px;top:68px;width:65px"><b>Your description text</b>Quickly repurpose top-line innovation before global communities.</div>
  <div class="dot" style="left:152px;top:101px;width:13px;height:13px"><svg viewBox="0 0 10 10"><path d="M2 8h6M3 4v4M5 4v4M7 4v4M2 4l3-2 3 2z" stroke="#fff" fill="none" stroke-width=".8"/></svg></div>
  <div class="item" style="left:183px;top:102px;width:65px"><b>Your description text</b>Quickly repurpose top-line innovation before global communities.</div>
  <div class="foot">Brisco Energy <small>a renewable energy services company</small></div>
  <div class="pg">www.brisco-energy.xyz &nbsp;|&nbsp; 18</div>
</section>

<!-- Row 7 -->
<section class="slide c1 r7">
  <div class="brand sm" style="left:232px;top:7px">Brisco</div>
  <div class="a" style="left:17px;top:12px;font-size:5.5px;font-weight:700;color:#111">Real <span style="color:var(--blue)">Statistic</span></div>
  <div class="a sub" style="left:17px;top:21px">Quickly repurpose top-line innovation before global communities</div>
  <div class="a pl" style="left:17px;top:40px;width:70px">Lorem Ipsum is simply dummy text of the printing Lorem Ipsum is simply dummy text</div>
  <div class="bars" style="left:16px;top:30px;width:132px;height:89px">
    <div class="bar" style="width:5px"><div class="b" style="height:2px;background:#3a4452"></div><div class="t" style="height:6px;background:var(--blue)"></div></div>
    <div class="bar" style="width:5px"><div class="b" style="height:5px;background:#3a4452"></div><div class="t" style="height:11px;background:var(--blue)"></div></div>
    <div class="bar" style="width:5px"><div class="b" style="height:4px;background:#3a4452"></div><div class="t" style="height:7px;background:var(--blue)"></div></div>
    <div class="bar" style="width:5px"><div class="b" style="height:2px;background:#3a4452"></div><div class="t" style="height:9px;background:var(--blue)"></div></div>
    <div class="bar" style="width:5px"><div class="b" style="height:3px;background:#3a4452"></div><div class="t" style="height:27px;background:var(--blue)"></div></div>
    <div class="bar" style="width:5px"><div class="b" style="height:10px;background:#3a4452"></div><div class="t" style="height:22px;background:var(--blue)"></div></div>
    <div class="bar" style="width:5px"><div class="b" style="height:6px;background:#3a4452"></div><div class="t" style="height:21px;background:var(--blue)"></div></div>
    <div class="bar" style="width:5px"><div class="b" style="height:10px;background:#3a4452"></div><div class="t" style="height:25px;background:var(--blue)"></div></div>
    <div class="bar" style="width:5px"><div class="b" style="height:13px;background:#3a4452"></div><div class="t" style="height:25px;background:var(--blue)"></div></div>
    <div class="bar" style="width:5px"><div class="b" style="height:10px;background:#3a4452"></div><div class="t" style="height:45px;background:var(--blue)"></div></div>
    <div class="bar" style="width:5px"><div class="b" style="height:25px;background:#3a4452"></div><div class="t" style="height:56px;background:var(--blue)"></div></div>
    <div class="bar" style="width:5px"><div class="b" style="height:4px;background:#3a4452"></div><div class="t" style="height:80px;background:var(--blue)"></div></div>
  </div>
  <div class="months" style="left:15px;top:122px;width:134px"><span>Jan</span><span>Feb</span><span>Mar</span><span>Apr</span><span>May</span><span>Jun</span><span>Jul</span><span>Aug</span><span>Sep</span><span>Oct</span><span>Nov</span><span>Dec</span></div>
  <div class="a" style="left:169px;top:31px;font-size:4.5px;color:#555;white-space:nowrap;font-weight:300">75<small style="font-size:2px">%</small> &nbsp;|&nbsp; 2,000<small style="font-size:2px">/for Day</small> &nbsp;|&nbsp; 850 <small style="font-size:2px">Users</small></div>
  <div class="dot sky" style="left:168px;top:51px"><svg viewBox="0 0 10 10"><path d="M2 5l6-3-3 6-1-2z" fill="#fff"/></svg></div>
  <div class="item" style="left:184px;top:50px;width:62px"><b>SERVICES <span class="sub">NAME</span></b>Quickly repurpose top-line innovation before global communities</div>
  <div class="dot" style="left:168px;top:74px"><svg viewBox="0 0 10 10"><rect x="2" y="2" width="6" height="6" fill="none" stroke="#fff"/></svg></div>
  <div class="item" style="left:184px;top:73px;width:62px"><b>SERVICES <span class="sub">NAME</span></b>Quickly repurpose top-line innovation before global communities</div>
  <div class="rule" style="left:170px;top:95px;width:10px"></div>
  <div class="a" style="left:170px;top:99px;width:76px;font-size:2px;line-height:1.6;color:#888">Make a positive impression with this clean and strong presentation template. Everything you need for a powerful and convincing talk, with charts and maps included.</div>
  <div class="foot">Brisco Energy <small>a renewable energy services company</small></div>
  <div class="pg">www.brisco-energy.xyz &nbsp;|&nbsp; 19</div>
</section>

<section class="slide c2 r7">
  <div class="brand sm" style="left:232px;top:7px">Brisco</div>
  <div class="a" style="left:0;top:7px;width:261px;text-align:center;font-size:5.5px;font-weight:500;color:#111"><span style="color:var(--blue)">Simple</span> Table</div>
  <div class="a sub" style="left:0;top:15px;width:261px;text-align:center">Quickly repurpose top-line innovation before global communities</div>
  <table class="grid a" style="left:15px;top:29px;width:230px">
    <tr><th>The Concepts</th><th>The Bara Name</th><th>The Bara Name</th><th>The Bara Name</th><th>The Bara Name</th><th>The Bara Name</th></tr>
    <tr><td>The Bara Name</td><td></td><td></td><td></td><td></td><td></td></tr>
    <tr><td>The Bara Name</td><td></td><td></td><td></td><td></td><td></td></tr>
    <tr><td>The Bara Name</td><td></td><td></td><td></td><td></td><td></td></tr>
    <tr><td>The Bara Name</td><td></td><td></td><td></td><td></td><td></td></tr>
    <tr><td>The Bara Name</td><td></td><td></td><td></td><td></td><td></td></tr>
    <tr><td>The Bara Name</td><td></td><td></td><td></td><td></td><td></td></tr>
  </table>
  <div class="a it" style="left:0;top:124px;width:261px;text-align:center;font-size:2.6px">"Neque porro quisquam est qui dolorem ipsum quia dolor sit amet, consectetur, adipisci velit..."</div>
  <div class="foot">Brisco Energy <small>a renewable energy services company</small></div>
  <div class="pg">www.brisco-energy.xyz &nbsp;|&nbsp; 20</div>
</section>

<section class="slide c3 r7">
  <div class="brand sm" style="left:232px;top:7px">Brisco</div>
  <div class="a" style="left:0;top:7px;width:261px;text-align:center;font-size:5.5px;font-weight:500;color:#111"><span style="color:var(--blue)">Simple</span> Table</div>
  <div class="a sub" style="left:0;top:15px;width:261px;text-align:center">Quickly repurpose top-line innovation before global communities</div>
  <table class="cal a" style="left:16px;top:32px;width:230px;table-layout:fixed">
    <tr><th>Monday</th><th>Tuesday</th><th>Wednesday</th><th>Thursday</th><th>Friday</th><th>Saturday</th><th>Sunday</th></tr>
    <tr><td>30</td><td>31</td><td>01<div class="ev" style="width:63px">Company event</div></td><td>02</td><td>03</td><td>04</td><td>05</td></tr>
    <tr><td>06</td><td>07</td><td>08</td><td>09</td><td>10<div class="ev" style="width:63px">Quarterly review</div></td><td>11</td><td>12</td></tr>
    <tr><td>13</td><td>14</td><td>15</td><td>16</td><td>17</td><td>18</td><td>19</td></tr>
    <tr><td>20</td><td>21<div class="ev" style="width:30px">Site visit</div></td><td>22</td><td>23</td><td>24</td><td>25</td><td>26</td></tr>
    <tr><td>27</td><td>28</td><td>29</td><td>30</td><td>01</td><td>02</td><td>03</td></tr>
    <tr><td>04</td><td>05</td><td>06</td><td>07</td><td>08</td><td>09</td><td>10</td></tr>
  </table>
  <div class="foot">Brisco Energy <small>a renewable energy services company</small></div>
  <div class="pg">www.brisco-energy.xyz &nbsp;|&nbsp; 21</div>
</section>

</body>
</html>
```